CD-Design für aufstrebende Newcomer Band
Zielgruppe
Wir sind eine Band (2 Brüder/ 20 und 23 Jahre alt) die ihre Debut-EP veröffentlichen.
Zielgruppe ist eher weiblich und jung (25 und jünger).
Die Band ist im Genre Pop / Singer-Songwriter.
http://www.funkenpaar-musik.de/
Songs sind in diesem Stil:
https://www.klangfilmportal.de/watch?v=Rb7tKm2Lq9x
https://www.klangfilmportal.de/watch?v=Hn4wXe8Pz3d
https://www.klangfilmportal.de/watch?v=Gs2vYc6Nj5t
Aufgabenstellung
Gesucht wird Design für CD + Cover + Inlay + Rückseite
Werbung des Designers im Inlay möglich.
Alle Dateien von uns (Logo, Fotos, Songtexte) können hier gefunden werden:
https://www.ablagekiste-online.de/sh/k3rw8m1tq52xb7z/BBQxLp4Fn2HeR_7TzmWk9aJd?dl=0
Die EP heißt: Nordlicht
Bitte unsere Gesichter gut platzieren (ist unsere erste CD und Fans sollen uns sofort wiedererkennen bzw unsere Gesichter als Marke positionieren)
Thema muss nicht unbedingt auf 'Nordlicht' gestützt sein.
Bitte die Schrift nicht in diesem Style, wie diese Sendung:
http://www.talfunk-sender.de/programm/sendungen/s-z/Sternwind_logo100~_v-box__16__9_-c41e7b2f90da63d85e1a2b47c9f0e13a6d8b5c27.png
Folgende Songs sind auf der EP (Rückseite):
1. Regen-Glanz
2. Wellen
3. Still Gehen
4. Spiegel
5. Nordlicht
6. Funken
7. Ihr
8. Regen-Glanz (Akustik)
9. Nordlicht (Akustik)
10. Nordlicht (Lindhalt Remix)
Produziert von T.B.Klangwerkstatt

```html
<!DOCTYPE html>
<html lang="de">
<head>
<meta charset="utf-8">
<title>Funkenpaar – Nordlicht</title>
<link rel="stylesheet" href="https://fonts.googleapis.com/css2?family=Roboto:wght@300;400;500&display=swap">
<style>
  :root {
    --paper: #ffffff;
    --ink-light: #ffffff;
    --disc: #1e1e1c;
    --front-dark: #4a211b;
    --front-mid: #7a3b30;
    --back-light: #d99c92;
    --back-mid: #b56a60;
  }
  html, body { margin: 0; padding: 0; overflow: hidden; }
  body {
    width: 1200px; height: 1083px; background: var(--paper);
    position: relative; font-family: "Roboto", sans-serif; color: var(--ink-light);
  }
  .panel {
    position: absolute; left: 118px; width: 460px; height: 460px; overflow: hidden;
    box-shadow: 0 1px 4px rgba(0,0,0,.25);
  }
  .front { top: 55px; }
  .back { top: 552px; }
  .photo { position: absolute; inset: 0; }
  .front .photo {
    background: radial-gradient(ellipse at 50% 45%, var(--front-mid), var(--front-dark) 80%);
  }
  .back .photo {
    background: linear-gradient(160deg, var(--back-mid) 0%, var(--back-light) 55%, var(--back-mid) 100%);
  }
  .title-grid { position: absolute; inset: 0; }
  .title-grid span {
    position: absolute; font-weight: 400; font-size: 120px; line-height: 1;
    transform: translate(-50%, -100%);
  }
  .band-name {
    position: absolute; left: 50%; transform: translateX(-50%);
    font-weight: 300; font-size: 17px; letter-spacing: 3px; white-space: nowrap;
  }
  .front .band-name { top: 470px; top: 472px; }
  .tracklist {
    position: absolute; top: 22px; left: 0; width: 100%; margin: 0; padding: 0;
    list-style: none; text-align: center;
  }
  .tracklist li { height: 29px; }
  .track-no { display: block; font-size: 5px; font-weight: 500; line-height: 8px; }
  .track-title { font-size: 10px; font-weight: 500; letter-spacing: 2px; line-height: 12px; }
  .track-note { font-size: 5px; font-weight: 500; letter-spacing: 1px; margin-left: 4px; }
  .credit {
    position: absolute; top: 346px; width: 100%; text-align: center;
    font-size: 5px; font-weight: 500; letter-spacing: 1px;
  }
  .back .band-name { top: 419px; }
  .disc { position: absolute; left: 664px; top: 64px; }
</style>
</head>
<body>

<section class="panel front">
  <div class="photo" role="img" aria-label="Foto der zwei Bandmitglieder in Sesseln, dazwischen eine Akustikgitarre, rötlich getönt"></div>
  <div class="title-grid">
    <span style="left:74px;top:137px">N</span>
    <span style="left:225px;top:137px">O</span>
    <span style="left:371px;top:137px">R</span>
    <span style="left:74px;top:264px">D</span>
    <span style="left:225px;top:264px">L</span>
    <span style="left:371px;top:264px">I</span>
    <span style="left:74px;top:389px">C</span>
    <span style="left:225px;top:389px">H</span>
    <span style="left:371px;top:389px">T</span>
  </div>
  <div class="band-name">FUNKENPAAR</div>
</section>

<section class="panel back">
  <div class="photo" role="img" aria-label="Foto eines Musikers mit Gitarre am Klavier, rosa getönt"></div>
  <ol class="tracklist">
    <li><span class="track-no">1</span><span class="track-title">REGEN-GLANZ</span></li>
    <li><span class="track-no">2</span><span class="track-title">WELLEN</span></li>
    <li><span class="track-no">3</span><span class="track-title">STILL GEHEN</span></li>
    <li><span class="track-no">4</span><span class="track-title">SPIEGEL</span></li>
    <li><span class="track-no">5</span><span class="track-title">NORDLICHT</span></li>
    <li><span class="track-no">6</span><span class="track-title">FUNKEN</span></li>
    <li><span class="track-no">7</span><span class="track-title">IHR</span></li>
    <li><span class="track-no">8</span><span class="track-title">REGEN-GLANZ</span><span class="track-note">(AKUSTIK)</span></li>
    <li><span class="track-no">9</span><span class="track-title">NORDLICHT</span><span class="track-note">(AKUSTIK)</span></li>
    <li><span class="track-no">10</span><span class="track-title">NORDLICHT</span><span class="track-note">(LINDHALT REMIX)</span></li>
  </ol>
  <div class="credit">PRODUZIERT VON T.B.KLANGWERKSTATT</div>
  <div class="band-name">FUNKENPAAR</div>
</section>

<svg class="disc" width="442" height="442" viewBox="0 0 442 442" aria-label="CD Nordlicht">
  <defs>
    <clipPath id="disc-shape"><circle cx="221" cy="221" r="221"/></clipPath>
    <mask id="disc-hole">
      <rect width="442" height="442" fill="#fff"/>
      <circle cx="221" cy="221" r="28" fill="#000"/>
    </mask>
    <path id="credit-arc" d="M 427 221 A 206 206 0 0 1 15 221"/>
  </defs>
  <g mask="url(#disc-hole)">
    <circle cx="221" cy="221" r="221" fill="var(--disc)"/>
    <g clip-path="url(#disc-shape)" fill="var(--ink-light)" font-family="Roboto, sans-serif" font-size="120" text-anchor="middle">
      <text x="58" y="128">N</text>
      <text x="215" y="128">O</text>
      <text x="372" y="128">R</text>
      <text x="58" y="261">D</text>
      <text x="215" y="261">L</text>
      <text x="372" y="261">I</text>
      <text x="58" y="394">C</text>
      <text x="215" y="394">H</text>
      <text x="372" y="394">T</text>
    </g>
    <text x="221" y="297" fill="var(--ink-light)" font-family="Roboto, sans-serif" font-weight="300" font-size="17" letter-spacing="3" text-anchor="middle">FUNKENPAAR</text>
    <text fill="var(--ink-light)" font-family="Roboto, sans-serif" font-weight="500" font-size="5.5" letter-spacing="1">
      <textPath href="#credit-arc" startOffset="50%" text-anchor="middle">PRODUZIERT VON T.B.KLANGWERKSTATT</textPath>
    </text>
  </g>
</svg>

</body>
</html>
```